Design a label for Copper Harbor e liquid company

need a logo and five different fonts for each flavor
1. hooray hooray wow_ confetti cream cake
2. Red Velvet- red velvet Cake
3, Tiramisu- lady fingers soaked in expresso
4. Crumb Castle- apple cinnamon muffin
5. Glen Fold- blueberry turn over
these labels are going to be two different bottle sizes
30 ml and 60 ml with 3 different nicotine strengths
Target Market(s)
vapors that want dessert flavors
Industry/Entity Type
It Company
Contact Information for Business Card
will supply logo
Other font styles liked:
- custom
Colors
Designer to choose colors to be used in the design.
Requirements
Must have
- custom logo and fonts
Nice to have
- ai files for multi color foil label printing

```html
<!DOCTYPE html>
<html lang="en">
<head>
<meta charset="utf-8">
<title>Copper Harbor – Dessert Flavor Labels</title>
<link rel="stylesheet" href="https://fonts.googleapis.com/css2?family=Chewy&family=Fredoka:wght@600&family=Bowlby+One&family=Alfa+Slab+One&family=Chango&family=Fira+Sans+Condensed:wght@500;700&display=swap">
<style>
  :root {
    --page: #ffffff;
    --ink-light: #ffffff;
    --logo-ink: #1a1a1a;
    --logo-chip: #f3f0e6;
    --blue-top: #4a6fc9;
    --blue-bottom: #2a1c8a;
    --muffin-top: #f2a3a0;
    --muffin-bottom: #7a0e14;
    --tira-top: #111111;
    --tira-bottom: #1e1e1e;
    --velvet-top: #b02a9a;
    --velvet-bottom: #d1121c;
    --bday-top: #d9d9e6;
    --bday-mid: #f3a2c9;
    --bday-bottom: #33e0f0;
    --splash-a: #ff2f8e;
    --splash-b: #27c1e8;
    --splash-c: #ffd23a;
  }
  * { box-sizing: border-box; margin: 0; padding: 0; }
  html, body { width: 1200px; height: 889px; overflow: hidden; background: var(--page); }
  .canvas {
    width: 1200px; height: 889px;
    display: flex; align-items: center; justify-content: center; gap: 40px;
  }
  .label {
    position: relative;
    width: 190px; height: 280px;
    border-radius: 4px;
    overflow: hidden;
    color: var(--ink-light);
    text-align: center;
  }
  .label--glen { background: linear-gradient(180deg, var(--blue-top), var(--blue-bottom)); }
  .label--crumb { background: linear-gradient(180deg, var(--muffin-top), var(--muffin-bottom)); }
  .label--tiramisu { background: linear-gradient(180deg, var(--tira-top), var(--tira-bottom)); }
  .label--velvet { background: linear-gradient(180deg, var(--velvet-top), var(--velvet-bottom)); }
  .label--hooray { background: linear-gradient(180deg, var(--bday-top), var(--bday-mid) 50%, var(--bday-bottom)); }

  .brand {
    position: absolute; top: 22px; left: 0; right: 0;
    display: flex; justify-content: center;
  }
  .brand__name {
    background: var(--logo-chip);
    color: var(--logo-ink);
    font-family: "Fira Sans Condensed", sans-serif;
    font-weight: 700;
    font-size: 15px;
    letter-spacing: 0.5px;
    text-transform: uppercase;
    padding: 5px 10px;
    border-radius: 3px;
  }
  .splash {
    position: absolute; top: 70px; left: 20px;
    width: 150px; height: 110px;
    border-radius: 50% 40% 55% 45%;
    background: radial-gradient(circle at 40% 40%, var(--splash-a), var(--splash-b) 55%, transparent 75%);
    opacity: 0.8;
  }
  .label--tiramisu .splash { background: radial-gradient(circle at 40% 40%, var(--splash-a), var(--splash-b) 50%, transparent 75%); }
  .flavor {
    position: absolute; left: 8px; right: 8px; top: 110px;
    line-height: 0.95;
    transform: rotate(-8deg);
  }
  .flavor--glen { font-family: "Chewy", cursive; font-size: 34px; color: #fff8d8; }
  .flavor--crumb { font-family: "Fredoka", sans-serif; font-weight: 600; font-size: 28px; color: #ffd7d2; }
  .flavor--tiramisu { font-family: "Bowlby One", sans-serif; font-size: 24px; color: #f6d8c4; top: 125px; }
  .flavor--velvet { font-family: "Alfa Slab One", serif; font-size: 30px; color: #ffe4ee; }
  .flavor--hooray { font-family: "Chango", sans-serif; font-size: 18px; color: #f6e8ff; line-height: 1.15; }

  .description {
    position: absolute; left: 14px; top: 200px;
    width: 110px;
    font-family: "Fira Sans Condensed", sans-serif;
    font-weight: 500;
    font-size: 14px; line-height: 1.05;
    text-align: left;
    transform: rotate(-8deg);
  }
  .label--velvet .description { font-size: 20px; top: 210px; left: 40px; }
  .dessert {
    position: absolute; right: 14px; top: 195px;
    width: 46px; height: 44px;
    border-radius: 8px;
  }
  .dessert--blueberry { background: linear-gradient(135deg, #7fb2ff, #2b3ea8); border-radius: 50%; top: 178px; height: 24px; width: 60px; }
  .dessert--muffin { background: linear-gradient(180deg, #9fe0ff, #f4c98a); }
  .dessert--tiramisu { background: linear-gradient(180deg, #8a5a36, #f2e3cc 50%, #6b4325); }
  .dessert--cake { background: linear-gradient(180deg, #fff, #c8101c); }
  .dessert--birthday { background: linear-gradient(180deg, #ff9ac8, #f2b46a); border-radius: 50%; }
</style>
</head>
<body>
<main class="canvas">

  <section class="label label--glen">
    <div class="brand"><span class="brand__name">Copper Harbor</span></div>
    <div class="splash" role="img" aria-label="Colourful paint splash with flower and swirl decoration"></div>
    <h2 class="flavor flavor--glen">Glen<br>Fold</h2>
    <p class="description">blueberry<br>turn over</p>
    <div class="dessert dessert--blueberry" role="img" aria-label="Illustration of blueberries"></div>
  </section>

  <section class="label label--crumb">
    <div class="brand"><span class="brand__name">Copper Harbor</span></div>
    <div class="splash" role="img" aria-label="Colourful paint splash with flower and swirl decoration"></div>
    <h2 class="flavor flavor--crumb">Crumb<br>Castle</h2>
    <p class="description">apple<br>cinnamon<br>muffin</p>
    <div class="dessert dessert--muffin" role="img" aria-label="Illustration of a frosted muffin"></div>
  </section>

  <section class="label label--tiramisu">
    <div class="brand"><span class="brand__name">Copper Harbor</span></div>
    <div class="splash" role="img" aria-label="Colourful paint splash with flower and swirl decoration"></div>
    <h2 class="flavor flavor--tiramisu">Tiramisu</h2>
    <p class="description">lady fingers<br>soaked in<br>esspresso</p>
    <div class="dessert dessert--tiramisu" role="img" aria-label="Illustration of a tiramisu slice"></div>
  </section>

  <section class="label label--velvet">
    <div class="brand"><span class="brand__name">Copper Harbor</span></div>
    <div class="splash" role="img" aria-label="Colourful paint splash with flower and swirl decoration"></div>
    <h2 class="flavor flavor--velvet">Red<br>Velvet</h2>
    <p class="description">cake</p>
    <div class="dessert dessert--cake" role="img" aria-label="Illustration of a red velvet cake slice"></div>
  </section>

  <section class="label label--hooray">
    <div class="brand"><span class="brand__name">Copper Harbor</span></div>
    <div class="splash" role="img" aria-label="Colourful paint splash with flower and swirl decoration"></div>
    <h2 class="flavor flavor--hooray">hooray hooray<br>wow</h2>
    <p class="description">confetti<br>cream<br>cake</p>
    <div class="dessert dessert--birthday" role="img" aria-label="Illustration of a birthday cake with candles"></div>
  </section>

</main>
</body>
</html>
```